Chartered Professional Accounting Firm Needs a Business Card Design

We need a card design for an accounting firm based in Toronto, Ontario. The firm name is Leo Dart Professional Corporation. The owner of the firm is a chartered professional accountant and a certified general accountant. Services of the firm include 60% tax preparation and consulting and 40% financial statements for corporation year-end. We would like a modern design. The color could be black, white, gray, blue or other color to bring more confidence to clients. The logo of the firm should be included in the design. Thanks

Name: Leo Dart, CPA, CGA Address: 47 Amberfield Cres. Richmond Hill, ON M3K 7P2 Telephone: (416) 555-0137 Fax:(416) 555-0192 Email: leo@leodart.example

Accounting

```html
<!DOCTYPE html>
<html lang="en">
<head>
<meta charset="utf-8">
<title>Leo Dart Professional Corporation – Business Card</title>
<link rel="stylesheet" href="https://fonts.googleapis.com/css2?family=Marcellus&family=Arimo:wght@400&display=swap">
<style>
  :root {
    --brand-blue: #2f3fae;
    --brand-blue-light: #5463c4;
    --brand-gray: #9a9a9a;
    --ink-gray: #8c8c8c;
    --card-white: #ffffff;
    --page-bg: #e9e7e3;
  }
  * { box-sizing: border-box; margin: 0; padding: 0; }
  html, body { width: 1200px; height: 1023px; overflow: hidden; }
  body {
    background: var(--page-bg);
    display: flex;
    flex-direction: column;
    align-items: center;
    justify-content: center;
    gap: 60px;
    font-family: "Marcellus", serif;
  }
  .card {
    position: relative;
    width: 700px;
    height: 400px;
    background: var(--card-white);
    box-shadow: 0 4px 18px rgba(0,0,0,0.15);
    overflow: hidden;
  }
  .card-band { position: absolute; inset: 0; }

  /* shared wordmark */
  .wordmark { display: flex; align-items: center; gap: 14px; }
  .wordmark-square { background: var(--brand-blue); flex: none; }
  .wordmark-name {
    color: var(--brand-blue);
    text-transform: uppercase;
    line-height: 1;
  }
  .tagline {
    color: var(--ink-gray);
    text-transform: uppercase;
    letter-spacing: 2px;
    line-height: 1.25;
  }

  /* front */
  .front .wordmark { position: absolute; left: 44px; top: 52px; }
  .front .wordmark-square { width: 56px; height: 56px; }
  .front .wordmark-name { font-size: 27px; }
  .front .wordmark-name small { display: block; font-size: 13px; letter-spacing: 1px; margin-top: 4px; }
  .front .tagline { position: absolute; left: 114px; top: 118px; font-size: 11px; }
  .person { position: absolute; left: 44px; top: 220px; }
  .person-name { color: var(--brand-blue); font-size: 34px; text-transform: uppercase; letter-spacing: 1px; }
  .person-title { color: var(--brand-gray); font-size: 24px; letter-spacing: 1px; margin-top: 4px; }
  .contact-list {
    position: absolute;
    left: 352px;
    top: 236px;
    list-style: none;
    font-family: "Arimo", sans-serif;
    font-size: 14px;
    color: var(--card-white);
  }
  .contact-list li { display: flex; align-items: center; gap: 10px; height: 30px; white-space: nowrap; }
  .contact-icon { width: 16px; height: 16px; flex: none; }

  /* back */
  .back .mark-square {
    position: absolute;
    left: 285px; top: 60px;
    width: 130px; height: 130px;
    background: var(--brand-blue);
  }
  .back .wordmark-block { position: absolute; left: 0; right: 0; top: 230px; text-align: center; }
  .back .wordmark-name { font-size: 46px; }
  .back .wordmark-name small { display: block; font-size: 20px; letter-spacing: 1px; margin-top: 6px; }
  .back .tagline { font-size: 15px; margin-top: 8px; }
</style>
</head>
<body>

  <section class="card front" aria-label="Business card front">
    <svg class="card-band" viewBox="0 0 700 400" aria-hidden="true">
      <defs>
        <linearGradient id="band-fill" x1="0" y1="1" x2="1" y2="0">
          <stop offset="0" stop-color="#5a66c6"/>
          <stop offset="1" stop-color="#2f3fae"/>
        </linearGradient>
      </defs>
      <path d="M700 60 C620 150 480 160 400 175 C320 190 280 280 260 400 L700 400 Z" fill="url(#band-fill)"/>
    </svg>

    <div class="wordmark">
      <span class="wordmark-square"></span>
      <div class="wordmark-name">Leo Dart<small>Professional Corporation</small></div>
    </div>
    <p class="tagline">Chartered Professional Accountant<br>Certified General Accountant</p>

    <div class="person">
      <p class="person-name">Leo Dart</p>
      <p class="person-title">CPA, CGA</p>
    </div>

    <ul class="contact-list">
      <li>
        <svg class="contact-icon" viewBox="0 0 16 16" aria-label="Phone"><path d="M4 1l3 3-2 2c1 2 3 4 5 5l2-2 3 3-2 2C7 14 2 9 2 3z" fill="#fff"/></svg>
        (416) 555-0137
      </li>
      <li>
        <svg class="contact-icon" viewBox="0 0 16 16" aria-label="Fax"><rect x="4" y="1" width="8" height="5" fill="none" stroke="#fff" stroke-width="1.5"/><rect x="1" y="6" width="14" height="7" fill="#fff"/><rect x="4" y="10" width="8" height="5" fill="#fff" stroke="#2f3fae"/></svg>
        (416) 555-0192
      </li>
      <li>
        <svg class="contact-icon" viewBox="0 0 16 16" aria-label="Email"><rect x="1" y="3" width="14" height="10" fill="none" stroke="#fff" stroke-width="1.5"/><path d="M1 3l7 6 7-6" fill="none" stroke="#fff" stroke-width="1.5"/></svg>
        leo@leodart.example
      </li>
      <li>
        <svg class="contact-icon" viewBox="0 0 16 16" aria-label="Address"><path d="M8 15C4 10 3 8 3 6a5 5 0 0110 0c0 2-1 4-5 9z" fill="#fff"/><circle cx="8" cy="6" r="2" fill="#2f3fae"/></svg>
        47 Amberfield Cres. Richmond Hill, ON M3K 7P2
      </li>
    </ul>
  </section>

  <section class="card back" aria-label="Business card back">
    <span class="mark-square"></span>
    <div class="wordmark-block">
      <div class="wordmark-name">Leo Dart<small>Professional Corporation</small></div>
      <p class="tagline">Chartered Professional Accountant<br>Certified General Accountant</p>
    </div>
  </section>

</body>
</html>
```